3 Flyer Project: Industrial, Civil, and Commercial

Total of 3 separate flyers that go together to be put in folders for marketing. The three flyer categories will be Industrial, Civil, and Commercial. I will upload three photos for each flyer and verbiage for each flyer. The photos may change upon final revisions. We want creativity and not just bullet points on a page.

FLYER #1 INDUSTRIAL

INDUSTRIAL EXPERIENCE:
BRELLANT COMPANY
VESKAR
OAKMOOR PIT MINE
GALDWYN FORGE STEEL
PERNOTH QUARTZWORKS
DUNMARROW VALE LOOP RAILWAY

INDUSTRIAL FOCUS AREAS:
PLANT FACILITY WATER SYSTEMS
HEAVY CONCRETE
FACILITY REPAIR
INDUSTRIAL UPGRADES
RAILWAYS AND MANUFACTURING

INDUSTRIAL SOLUTIONS:
WE MAINTAIN AN EXTENSIVE LEVEL OF DETAIL AND INNOVATIVE PROBLEM-SOLVING TALENTS TO DELIVER HIGH QUALITY, SUSTAINABLE SOLUTIONS.

FLYER #2 CIVIL

CIVIL EXPERIENCE:
VELDORAN DEPT. OF TRANSPORTATION
KESTRIA DEPT. OF TRANSPORTATION
PLOVENDA DEPT. OF TRANSPORTATION
BUREAU OF WORKSMITHS
NATIONAL SKYWAYS AUTHORITY BOARD
MINISTRY OF GUARDIANSHIP

CIVIL FOCUS AREAS:
AIRFIELD
STREETSCAPES
STORM DRAINAGE
UTILITY UPGRADES
BOX CULVERTS
RETAINING WALLS

CIVIL SOLUTIONS:
WE SPECIALIZE IN COMPLEX CIVIL PROJECTS.

FLYER #3 COMMERCIAL

COMMERCIAL EXPERIENCE:
HOLLENBRAKE UPLANDS UNIVERSITY
VELDORAN OFFICE OF STRUCTURES
TOWN OF BRANWICK, MISSISSIPPI
TOWN OF MERRODA, MISSISSIPPI
ACADEMY FOR ADVANCED STUDIES

COMMERCIAL FOCUS AREAS:
NEW CONSTRUCTION
RENOVATIONS
STRUCTURAL FOUNDATIONS
STRUCTURAL UPGRADES

COMMERCIAL SOLUTIONS:
WE NOT ONLY KNOW HOW ALL THE PARTS AND PIECES FIT TOGETHER WITHIN A PROJECT, BUT WE SPECIALIZE IN THE SELF PERFORMANCE OF MANY DIVISIONS WHICH DIFFERENTIATES US FROM MANY OTHER GENERAL CONTRACTORS.

Marketing

• 3 photos on each flyer based on the Industrial, Commercial, and Civil flyers description. Our company logo as well as descriptions shown for each flyer. The blue we use in our logo cmyk is 100-80-0-22

```html
<!DOCTYPE html>
<html lang="en">
<head>
<meta charset="utf-8">
<title>Harrowgate Construction – Industrial Flyer</title>
<link rel="stylesheet" href="https://fonts.googleapis.com/css2?family=Roboto+Condensed:wght@700&family=Lato:wght@400;700&display=swap">
<style>
  :root {
    --navy: #263b8d;
    --ink: #2e2e2e;
    --text: #1f1f1f;
    --band-grey: #d8d7d7;
    --page: #ffffff;
    --backdrop: #3a3a3a;
  }
  * { margin: 0; padding: 0; box-sizing: border-box; }
  html, body { width: 1200px; height: 1200px; overflow: hidden; }
  body { background: var(--backdrop); position: relative; font-family: "Lato", sans-serif; }

  .flyer {
    position: absolute; left: 154px; top: 24px;
    width: 990px; height: 1280px;
    background: var(--page);
    transform: scale(0.9); transform-origin: top left;
    overflow: hidden;
  }
  .abs { position: absolute; }

  .hero { left: 0; top: 0; width: 990px; height: 600px; }

  .headline {
    left: 247px; top: 58px;
    font-family: "Roboto Condensed", sans-serif; font-weight: 700;
    font-size: 56px; line-height: 58px; letter-spacing: 1.5px;
  }
  .headline .line-one { color: var(--ink); display: block; }
  .headline .line-two { color: var(--navy); display: block; }

  .brand { left: 192px; top: 564px; width: 374px; display: flex; align-items: center; gap: 12px; }
  .brand-square { width: 96px; height: 96px; background: var(--navy); flex: none; }
  .brand-name {
    width: 266px;
    font-family: "Roboto Condensed", sans-serif; font-weight: 700; color: var(--navy);
    text-align: center; line-height: 1; white-space: nowrap;
  }
  .brand-name .main { display: block; font-size: 47px; letter-spacing: 0; }
  .brand-name .sub {
    display: flex; align-items: center; gap: 8px;
    font-size: 28px; margin-top: 8px; letter-spacing: 0.3px; color: var(--navy);
  }
  .brand-name .sub::before,
  .brand-name .sub::after { content: ""; flex: 1; height: 2px; background: var(--navy); }

  .photo-street { left: 587px; top: 414px; width: 403px; height: 236px; background: linear-gradient(180deg, #cfe0ee 0%, #c9bba6 55%, #b69c86 100%); }
  .band { background: var(--band-grey); height: 18px; left: 584px; width: 406px; }
  .band-upper { top: 657px; }
  .band-lower { top: 925px; }

  .solutions {
    left: 584px; top: 682px; width: 406px; height: 238px;
    background: var(--navy); color: #fff; text-align: center;
    padding: 30px 34px 0;
  }
  .solutions h2 { font-family: "Lato", sans-serif; font-weight: 400; font-size: 38px; line-height: 46px; letter-spacing: 0.5px; }
  .solutions p { font-size: 15px; line-height: 19.5px; margin-top: 20px; }

  .photo-sunset { left: 584px; top: 948px; width: 406px; height: 233px; background: linear-gradient(180deg, #6f86b3 0%, #c79aa0 45%, #f0b36a 75%, #e38a44 100%); }

  .section-title { font-size: 26px; font-weight: 400; letter-spacing: 0.3px; }
  .focus-title { left: 40px; top: 716px; color: var(--text); }
  .focus-list { left: 40px; top: 770px; list-style: none; }
  .focus-list li { display: flex; align-items: center; height: 48.5px; font-size: 20px; color: var(--text); }
  .focus-list svg { width: 34px; height: 34px; margin-right: 27px; flex: none; }

  .experience-title { left: 40px; top: 1044px; color: var(--navy); }
  .clients { left: 40px; top: 1092px; width: 526px; display: flex; justify-content: space-between; align-items: center; gap: 8px; }
  .client { font-size: 10px; font-weight: 700; color: var(--navy); text-align: center; line-height: 12px; width: 80px; }

  .footer { left: 0; top: 1187px; width: 990px; height: 93px; background: var(--navy); }
  .footer-rule { left: 0; top: 1194px; width: 990px; height: 3px; background: #fff; opacity: 0.9; }
  .footer-info {
    left: 38px; top: 1216px; width: 920px;
    display: flex; align-items: center; color: #fff; font-size: 16px;
  }
  .footer-info span { display: flex; align-items: center; }
  .footer-info svg { width: 24px; height: 24px; margin-right: 12px; }
  .footer-info .web { margin-left: 32px; }
  .footer-info .phone { margin-left: 28px; }
</style>
</head>
<body>
<div class="flyer">
  <svg class="abs hero" viewBox="0 0 990 600" role="img" aria-label="Photo of a downtown street under construction with workers in safety vests and excavators beside old brick buildings">
    <defs>
      <linearGradient id="heroTone" x1="0" y1="0" x2="0" y2="1">
        <stop offset="0" stop-color="#f7f7f6"/>
        <stop offset="0.35" stop-color="#e6e3de"/>
        <stop offset="0.7" stop-color="#c5b7a2"/>
        <stop offset="1" stop-color="#a99883"/>
      </linearGradient>
    </defs>
    <polygon points="0,0 990,0 990,388 519,388 111,578 0,533" fill="url(#heroTone)"/>
    <polyline points="990,396 523,396 112,587 0,542" fill="none" stroke="var(--navy)" stroke-width="8"/>
  </svg>

  <h1 class="abs headline">
    <span class="line-one">QUALITY CONSTRUCTION</span>
    <span class="line-two">FIRST CLASS DELIVERY</span>
  </h1>

  <div class="abs brand">
    <div class="brand-square"></div>
    <div class="brand-name"><span class="main">HARROWGATE</span><span class="sub">CONSTRUCTION</span></div>
  </div>

  <div class="abs photo-street" role="img" aria-label="Photo of a finished streetscape with new sidewalks and lamp posts in a historic town"></div>
  <div class="abs band band-upper"></div>

  <section class="abs solutions">
    <h2>INDUSTRIAL<br>SOLUTIONS:</h2>
    <p>we maintain an extensive level of detail and innovative problem-solving talents to deliver high quality, sustainable solutions.</p>
  </section>
  <div class="abs band band-lower"></div>

  <div class="abs photo-sunset" role="img" aria-label="Photo of construction workers silhouetted against a sunset while placing steel rebar"></div>

  <h2 class="abs section-title focus-title">INDUSTRIAL FOCUS AREAS:</h2>
  <ul class="abs focus-list">
    <li><svg viewBox="0 0 34 34" fill="none" stroke="#333" stroke-width="2"><path d="M8 6h16v6h-4v6"/><path d="M3 26q4-3 7 0t7 0 7 0 7 0M3 31q4-3 7 0t7 0 7 0 7 0"/></svg>Plant Facility Water Systems</li>
    <li><svg viewBox="0 0 34 34"><polygon points="17,3 30,9 30,25 17,31 4,25 4,9" fill="#777"/><polygon points="17,3 30,9 17,15 4,9" fill="#bbb"/><polygon points="17,15 30,9 30,25 17,31" fill="#555"/></svg>Heavy Concrete</li>
    <li><svg viewBox="0 0 34 34"><path d="M27 4a7 7 0 0 0-8 9L5 27a3 3 0 0 0 4 4l14-14a7 7 0 0 0 9-8l-4 4-4-1-1-4z" fill="#333"/></svg>Facility Repair</li>
    <li><svg viewBox="0 0 34 34" fill="none" stroke="#555" stroke-width="1.6"><path d="M3 30V17l7 4v-4l7 4v-4l7 4V5h5v25z"/><path d="M7 25h2M12 25h2M17 25h2M22 25h2"/></svg>Industrial Upgrades</li>
    <li><svg viewBox="0 0 34 34" stroke="#222" stroke-width="3.5" stroke-linecap="round"><path d="M6 28L26 8M8 8l20 20"/><path d="M22 4l8 8" stroke-width="5"/></svg>Railways and Manufacturing</li>
  </ul>

  <h2 class="abs section-title experience-title">INDUSTRIAL EXPERIENCE:</h2>
  <div class="abs clients">
    <span class="client">DUNMARROW VALE LOOP RAILWAY</span>
    <span class="client">PERNOTH QUARTZWORKS</span>
    <span class="client">GALDWYN FORGE STEEL</span>
    <span class="client">OAKMOOR PIT MINE</span>
    <span class="client">VESKAR</span>
    <span class="client">BRELLANT COMPANY</span>
  </div>

  <div class="abs footer"></div>
  <div class="abs footer-rule"></div>
  <div class="abs footer-info">
    <span><svg viewBox="0 0 24 24" fill="#fff"><path d="M12 3L1 12h3v9h6v-6h4v6h6v-9h3z"/></svg>820 Foundry Row Road Branwick, Veldora 40812</span>
    <span class="web"><svg viewBox="0 0 24 24" fill="none" stroke="#fff" stroke-width="1.6"><circle cx="12" cy="12" r="9"/><ellipse cx="12" cy="12" rx="4" ry="9"/><path d="M3 12h18M5 7h14M5 17h14"/></svg>www.harrowgatebuild.com</span>
    <span class="phone"><svg viewBox="0 0 24 24" fill="none" stroke="#fff" stroke-width="1.8"><path d="M6 3l3 4-2 2a11 11 0 0 0 7 7l2-2 4 3-2 3C10 20 4 14 3 5z"/></svg>555-014-2290</span>
  </div>
</div>
</body>
</html>
```